A Gallery type Web design

We are developing a Wordpress based website for a client that does design construction projects. E.g. Pools, Lobbies, Toilets, etc. The website will mainly be to showcase their past projects and the collections they have.
No programming required, we just need the designs!
A sample of what the client is looking for:
http://velmora.it/
Pages to include:
• Home – A nice slider design to showcase selected photos
• Main Category Template
• Sub Category Template
• About us
• Contact us
Example of their Main Categories and their Sub Categories:
Collections - Granite
- Marble
- Sculpture
Projects - Private
- Public
- Commercial
- Overseas
Installation - Vanity tops
- Hall areas
- Toilets
The Main Category is to show a sample and link the user to the respective Sub Categories. The Sub Categories are to showcase all the photos they have from the category. Please leave a little space to add some text or caption for the photo.
Designs need to be mobile responsive!
I've attached their logo and some sample photos to use for mock ups. Let me know if you have any questions!

```html
<!DOCTYPE html>
<html lang="en">
<head>
<meta charset="utf-8">
<title>Granvale – Mobile Home</title>
<link rel="stylesheet" href="https://fonts.googleapis.com/css2?family=Lato:wght@400;700&family=Oswald:wght@400;500&display=swap">
<style>
  :root {
    --page-bg: #e4e2df;
    --white: #ffffff;
    --ink: #1f1f1f;
    --text: #555555;
    --muted: #777777;
    --rule: #d6d6d6;
    --accent: #d8232a;
    --nav-top: #f4f4f4;
    --nav-bottom: #d9d9d9;
    --btn: #1e1e1e;
    --band: #f1f1f1;
    --footer: #323232;
    --footer-deep: #2c2c2c;
    --footer-line: #4a4a4a;
    --footer-text: #e6e6e6;
    --social: #5a5a5a;
  }
  * { box-sizing: border-box; margin: 0; padding: 0; }
  html, body { width: 785px; height: 1200px; overflow: hidden; }
  body { background: var(--page-bg); font-family: "Lato", sans-serif; position: relative; }

  .screen { position: absolute; left: 263px; top: 105px; width: 253px; height: 918px; background: var(--white); overflow: hidden; }

  .site-header { height: 67px; display: flex; align-items: center; justify-content: center; gap: 7px; }
  .brand-mark { width: 12px; height: 12px; background: var(--accent); }
  .brand-name { font-family: "Lato", sans-serif; font-weight: 700; font-size: 19px; color: var(--accent); letter-spacing: 1px; }

  .toolbar { height: 25px; background: linear-gradient(var(--nav-top), var(--nav-bottom)); position: relative; border-top: 1px solid var(--rule); }
  .tool-btn { position: absolute; top: 2px; width: 22px; height: 20px; background: var(--btn); border-radius: 3px; display: flex; align-items: center; justify-content: center; }
  .tool-btn.menu { left: 27px; }
  .tool-btn.phone { left: 177px; }
  .tool-btn.mail { left: 203px; }

  .slider { height: 141px; position: relative; background: linear-gradient(160deg, #9a9893 0%, #5c5a55 45%, #2a2926 100%); }
  .slider-caption { position: absolute; left: 28px; top: 50px; width: 196px; height: 23px; background: rgba(40,40,40,.55); color: var(--white); font-family: "Oswald", sans-serif; font-size: 13px; line-height: 23px; text-align: center; }
  .slider-dots { position: absolute; left: 108px; top: 129px; display: flex; gap: 3px; }
  .slider-dots span { width: 6px; height: 6px; border-radius: 50%; background: var(--white); }
  .slider-dots span.active { background: var(--accent); }

  .about { padding: 10px 27px 0 26px; height: 407px; }
  .section-title { font-weight: 700; font-size: 11px; color: var(--ink); letter-spacing: .2px; }
  .title-rule { margin-top: 5px; height: 2px; background: var(--rule); position: relative; margin-bottom: 7px; }
  .title-rule::before { content: ""; position: absolute; left: 0; top: 0; width: 54px; height: 2px; background: var(--ink); }
  .about p { font-size: 6.6px; line-height: 9.85px; color: var(--text); text-align: justify; letter-spacing: .15px; margin-bottom: 11px; }
  .about-photo { margin-top: 2px; width: 198px; height: 130px; border: 1px solid var(--rule); padding: 2px; }
  .about-photo div { width: 100%; height: 100%; background: linear-gradient(90deg, #c9cccc 0%, #e4e6e4 45%, #8d6a4a 80%, #5b3e26 100%); }

  .latest { background: var(--band); height: 108px; padding: 8px 27px 0; border-top: 1px solid #e6e6e6; }
  .latest-title { font-family: "Oswald", sans-serif; font-size: 10px; color: var(--accent); margin-bottom: 8px; }
  .project { display: flex; gap: 5px; margin-bottom: 8px; }
  .project-thumb { width: 28px; height: 28px; border: 1px solid var(--rule); flex: none; }
  .project-thumb.one { background: linear-gradient(135deg, #d8d8d8, #b4b4b4); }
  .project-thumb.two { background: linear-gradient(135deg, #9fa3a6, #3e4447); }
  .project-name { font-size: 8px; color: var(--ink); line-height: 10px; }
  .project-text { font-size: 6.6px; color: var(--muted); line-height: 9px; width: 92px; }

  .footer { background: var(--footer); height: 117px; position: relative; color: var(--footer-text); border-top: 1px solid #222; }
  .footer-col { position: absolute; top: 12px; }
  .footer-col.nav { left: 27px; width: 49px; }
  .footer-col.contact { left: 125px; width: 105px; }
  .footer-divider { position: absolute; left: 104px; top: 6px; width: 1px; height: 108px; background: var(--footer-line); }
  .footer-heading { font-family: "Oswald", sans-serif; font-size: 9.5px; color: var(--footer-text); padding-bottom: 4px; border-bottom: 1px solid var(--footer-line); margin-bottom: 8px; }
  .footer-col.contact .footer-heading { border-bottom: none; }
  .nav-list { list-style: none; font-size: 7px; line-height: 11.2px; }
  .nav-list li::before { content: "›"; margin: 0 5px 0 2px; }
  .contact-row { display: flex; gap: 5px; font-size: 6.6px; line-height: 9px; margin-bottom: 8px; }
  .contact-row svg { flex: none; margin-top: 1px; }
  .contact-row strong { font-weight: 700; }
  .contact-row.phone-number { font-weight: 700; font-size: 8px; }

  .footer-bottom { background: var(--footer-deep); height: 53px; border-top: 1px solid var(--footer-line); padding: 7px 0 0 29px; color: var(--footer-text); }
  .social { display: flex; gap: 4px; margin-bottom: 8px; }
  .social span { width: 20px; height: 20px; border-radius: 3px; background: var(--social); }
  .copyright { font-size: 6.6px; }
</style>
</head>
<body>
<main class="screen">
  <header class="site-header">
    <span class="brand-mark"></span>
    <span class="brand-name">GRANVALE</span>
  </header>

  <nav class="toolbar">
    <div class="tool-btn menu">
      <svg width="12" height="10" viewBox="0 0 12 10"><path d="M0 1h12M0 5h12M0 9h12" stroke="#fff" stroke-width="1.4"/></svg>
    </div>
    <div class="tool-btn phone">
      <svg width="10" height="10" viewBox="0 0 10 10"><path d="M2 0.5l2 2.2-1 1.2c.6 1.2 1.6 2.2 2.8 2.8l1.2-1 2.2 2-1.2 1.8C4.5 9.3.7 5.5.5 2z" fill="#fff"/></svg>
    </div>
    <div class="tool-btn mail">
      <svg width="13" height="9" viewBox="0 0 13 9"><rect x=".6" y=".6" width="11.8" height="7.8" fill="none" stroke="#fff" stroke-width="1.1"/><path d="M.6.8l5.9 4.2L12.4.8" fill="none" stroke="#fff" stroke-width="1.1"/></svg>
    </div>
  </nav>

  <section class="slider" role="img" aria-label="Slider photo of a furnished lobby with a patterned tile floor">
    <div class="slider-caption">Lorem ipsum dolor sit amet adipiscing</div>
    <div class="slider-dots"><span class="active"></span><span></span><span></span><span></span></div>
  </section>

  <section class="about">
    <h2 class="section-title">ABOUT US</h2>
    <div class="title-rule"></div>
    <p>Lorem ipsum dolor sit amet, consectetuer adipiscing elit, sed diam nonummy nibh euismod tincidunt ut laoreet dolore magna aliquam erat volutpat. Ut wisi enim ad minim veniam, quis nostrud exerci tation ullamcorper suscipit lobortis nisl ut aliquip ex ea commodo consequat. Duis autem vel eum iriure dolor in hendrerit in vulputate velit esse molestie consequat, vel illum dolore eu feugiat nulla facilisis at vero eros et accumsan et iusto odio dignissim qui blandit praesent luptatum zzril delenit augue duis dolore te feugait nulla facilisi.</p>
    <p>Lorem ipsum dolor sit amet, consectetuer adipiscing elit, sed diam nonummy nibh euismod tincidunt ut laoreet dolore magna aliquam erat volutpat. Ut wisi enim ad minim veniam, quis nostrud exerci tation ullamcorper suscipit lobortis nisl ut aliquip ex ea commodo consequat. Duis autem vel eum</p>
    <p>iriure dolor in hendrerit in vulputate velit esse molestie consequat, vel illum dolore eu feugiat nulla facilisis at vero eros et accumsan et iusto odio dignissim qui blandit praesent luptatum zzril delenit augue duis dolore te feugait nulla facilisi. Lorem ipsum dolor sit amet, consectetuer adipiscing elit, sed</p>
    <div class="about-photo"><div role="img" aria-label="Photo of the showroom reception with a glass door and wooden panelling"></div></div>
  </section>

  <section class="latest">
    <h3 class="latest-title">Latest Projects</h3>
    <div class="project">
      <div class="project-thumb one" role="img" aria-label="Thumbnail of a marble project"></div>
      <div><div class="project-name">Lorem ipsum dolor</div><div class="project-text">Lorem ipsum dolor sit amet adipiscing</div></div>
    </div>
    <div class="project">
      <div class="project-thumb two" role="img" aria-label="Thumbnail of a lobby project"></div>
      <div><div class="project-name">Lorem ipsum dolor</div><div class="project-text">Lorem ipsum dolor sit amet adipiscing</div></div>
    </div>
  </section>

  <footer>
    <div class="footer">
      <div class="footer-col nav">
        <h4 class="footer-heading">Navigation</h4>
        <ul class="nav-list">
          <li>Home</li><li>Collections</li><li>Projects</li><li>Installations</li><li>About Us</li><li>Contact Us</li>
        </ul>
      </div>
      <div class="footer-divider"></div>
      <div class="footer-col contact">
        <h4 class="footer-heading">Contact Us</h4>
        <div class="contact-row">
          <svg width="7" height="10" viewBox="0 0 7 10"><path d="M3.5 0A3.5 3.5 0 0 0 0 3.5C0 6 3.5 10 3.5 10S7 6 7 3.5A3.5 3.5 0 0 0 3.5 0zm0 5a1.4 1.4 0 1 1 0-2.8 1.4 1.4 0 0 1 0 2.8z" fill="#e6e6e6"/></svg>
          <div><strong>Lorem ipsum dolor sit amet</strong><br>consectetuer adimpisciged<br>diamr nonummy nibh</div>
        </div>
        <div class="contact-row phone-number">
          <svg width="8" height="8" viewBox="0 0 10 10"><path d="M2 0.5l2 2.2-1 1.2c.6 1.2 1.6 2.2 2.8 2.8l1.2-1 2.2 2-1.2 1.8C4.5 9.3.7 5.5.5 2z" fill="#e6e6e6"/></svg>
          <div>123 456 7890</div>
        </div>
        <div class="contact-row">
          <svg width="8" height="7" viewBox="0 0 8 7"><path d="M0 3l4-3 4 3v4H0z" fill="#e6e6e6"/></svg>
          <div>info@granvalemktg.com</div>
        </div>
      </div>
    </div>
    <div class="footer-bottom">
      <div class="social"><span></span><span></span><span></span><span></span></div>
      <div class="copyright">© 2014 GranvaleMarketing. All Right Reserved</div>
    </div>
  </footer>
</main>
</body>
</html>
```